依頼詳細
ロゴを2色用意しておりますので、表と裏に使ってください。
記載項目
表面:会社名/役職/名前/住所/電話/Fax/Mail/HPアドレス
裏面:サイトURL
希望イメージ
シンプル 複雑
単色 カラフル
暗い 明るい
日常 高級
遊び心 厳粛
未来的 伝統的
女性的 男性的
希望する色
色の種類はお任せします。
納品ファイル
• 高解像度JPG (.jpg)
• イラストレーター形式 (.ai)
• フォトショップ形式 (.psd)
補足説明
宜しくお願いします。
シンプルかつ斬新な感じでお願いします。
ロゴの使い方はお任せいたします。
一応ロゴマークも添付いたします。マーク存在感がありますので、お使いにならなくてももちろん大丈夫です。
裏面にロゴを使っても使わなくても結構です。

会社名(ロゴでもOK)・名前・住所・tel・fax・mobile・Email

HPアドレス

最低限この情報を入れて頂ければ大丈夫です。
何卒宜しくお願いいたします。
何卒宜しくお願いします。
お世話になります。
ロゴ文字のデザイン(IT、テクノロジー)を気に入っておりますので、ロゴ文字に合わせて頂くデザインをお願いしたいと思います。

あと、やはり黒のロゴ文字金のロゴ文字を2面性を持たせる様な形で利用して頂きたいです。

宜しくお願いします。
料金を変更させて頂きました。
皆様ご提案頂きましてありがとうございます。

追記ばかりで申し訳ありません。

金の配色に関してですが、全面的に金色を出すよりも、控えめな形で出して頂ければ幸いです。

あと締めきり日を早めさせていただきます。

何卒宜しくお願いします。
■ 選んだ理由

ロゴに合わせて頂いたところです。

■ 提案者全員のお礼・コメント

この度はご提案頂きまして、誠にありがとうございました。

```html
<!DOCTYPE html>
<html lang="ja">
<head>
<meta charset="utf-8">
<title>Brightway Partners 名刺</title>
<link rel="stylesheet" href="https://fonts.googleapis.com/css2?family=Noto+Sans+JP:wght@400;500;700;900&display=swap">
<style>
  :root {
    --paper: #ffffff;
    --ink: #111111;
    --gold: #a9874a;
    --gold-dark: #6f5226;
    --gold-light: #c9a766;
    --edge: #b9b9b9;
  }
  * { margin: 0; padding: 0; box-sizing: border-box; }
  html, body { width: 802px; height: 1200px; overflow: hidden; background: var(--paper); }
  body { position: relative; font-family: "Noto Sans JP", sans-serif; color: var(--ink); }

  .card { position: absolute; left: 0; width: 802px; background: var(--paper); border: 2px solid var(--edge); }
  .card--front { top: 0; height: 502px; }
  .card--back { top: 668px; height: 532px; }

  .brand { position: absolute; display: flex; align-items: center; }
  .brand__dot { border-radius: 50%; background: radial-gradient(circle at 40% 35%, var(--gold-light), var(--gold) 55%, var(--gold-dark)); flex: none; }
  .brand__name { font-weight: 500; color: var(--gold); letter-spacing: 0.06em; white-space: nowrap; }

  .card--front .brand { left: 78px; top: 30px; }
  .card--front .brand__dot { width: 124px; height: 124px; }
  .card--front .brand__name { font-size: 50px; margin-left: 44px; margin-top: -30px; }
  .brand-rule { position: absolute; left: 236px; top: 172px; width: 500px; height: 3px; background: linear-gradient(90deg, var(--gold-dark), var(--gold-light), var(--gold-dark)); }

  .tagline { position: absolute; left: 0; right: 0; top: 182px; text-align: center; font-size: 38px; font-weight: 900; letter-spacing: 0.04em; }
  .tagline span { display: inline-block; padding: 0 8px 4px; border-bottom: 4px solid var(--gold); }
  .mission { position: absolute; left: 0; right: 0; top: 254px; text-align: center; font-size: 16px; font-weight: 700; }

  .person { position: absolute; left: 366px; top: 348px; }
  .person__title { font-size: 14px; font-weight: 500; }
  .person__name { font-size: 40px; font-weight: 500; letter-spacing: 0.12em; line-height: 1.2; }

  .card--back .brand { left: 98px; top: 724px; }
  .card--back .brand__dot { width: 62px; height: 62px; }
  .card--back .brand__name { font-size: 30px; margin-left: 18px; color: var(--ink); }
  .card--back .brand-rule { left: 186px; top: 786px; width: 270px; height: 2px; }

  .contact { position: absolute; left: 234px; top: 840px; font-size: 20px; font-weight: 700; line-height: 39px; }
  .contact__icon { display: inline-block; width: 20px; height: 18px; vertical-align: -2px; margin-right: 6px; }

  .site { position: absolute; left: 98px; top: 1076px; width: 636px; height: 62px; display: flex; align-items: center;
          background: linear-gradient(180deg, var(--gold-light), var(--gold) 45%, var(--gold-dark)); }
  .site__label { margin-left: 18px; background: var(--paper); color: var(--gold-dark); font-size: 18px; font-weight: 900; padding: 2px 8px; }
  .site__url { margin-left: 16px; color: var(--paper); font-size: 30px; font-weight: 700; letter-spacing: 0.01em; }
</style>
</head>
<body>
  <section class="card card--front">
    <div class="brand">
      <span class="brand__dot"></span>
      <span class="brand__name">Brightway Partners</span>
    </div>
    <div class="brand-rule"></div>
    <p class="tagline"><span>中小企業を強くする</span></p>
    <p class="mission">* インターネットサービス提供 Web 上を含めたビジネスマッチングを構築 *</p>
    <div class="person">
      <p class="person__title">代表取締役</p>
      <p class="person__name">森田　健一</p>
    </div>
  </section>

  <section class="card card--back"></section>
  <div class="brand" style="left:98px; top:724px;">
    <span class="brand__dot" style="width:62px;height:62px;"></span>
    <span class="brand__name" style="font-size:30px;margin-left:18px;color:var(--ink);">Brightway Partners</span>
  </div>
  <div class="brand-rule" style="left:186px; top:786px; width:270px; height:2px;"></div>

  <address class="contact" style="font-style:normal;">
    <div>〒105-0014</div>
    <div>東京都港区芝 4-5-6 南北ビル5F</div>
    <div><svg class="contact__icon" viewBox="0 0 20 18" aria-hidden="true"><path d="M2 5c0-3 16-3 16 0v2h-4V5H6v2H2z M4 9h12l2 8H2z" fill="#111"/></svg>03-5550-0101 fax 03-5550-0102</div>
    <div>mobile 090-5550-0303</div>
    <div>Email / info@brightway-mail.jp</div>
  </address>

  <div class="site">
    <span class="site__label">URL</span>
    <span class="site__url">http: www.brightwaypartners.com</span>
  </div>
</body>
</html>
```